Business Card for Multi-Brand Sportswear Company

We are looking for a business card which represents our company and the multiple brands within it.

The company: Kelt Athletic (LTD)
The brands: Kelt, PawaLuni, VerdantFlex, Grit and Gale

Employees using these cards would be representing Kelt Athletic, rather than any of the individual brands. You will see a current design within the uploaded files, to give some inspiration. The actual text of the brands is not necessary, but the logos should be on there is some format.

Our creative minds on this are stretched, so we are looking for someone to make this their own, and show us what a good business card should look like.

We may like to get these printed with spot gloss, so keep that in mind with your designs.

www.keltathletic.co.uk

Industry/Entity Type

Business

Contact Information for Business Card

Tom Hollingsworth-Pryce
Operations Manager
(+44) 1632 960 418
Tom@keltathletic.co.uk
www.keltathletic.co.uk

Font styles to use
Sans Serif
Other font styles liked:
• Eurostile

Colors
ffffff

Requirements
Nice to have
• Dark (black) background

```html
<!DOCTYPE html>
<html lang="en">
<head>
<meta charset="utf-8">
<title>Kelt Athletic – Business Card</title>
<link rel="stylesheet" href="https://fonts.googleapis.com/css2?family=Exo+2:wght@400;600;700&display=swap">
<style>
  :root {
    --page: #f2f2f2;
    --card-dark: #2b2b2b;
    --card-dark-2: #343434;
    --card-light: #f4f4f4;
    --card-light-2: #dcdcdc;
    --ink-white: #ffffff;
    --ink-soft: #d9d9d9;
    --ink-black: #1a1a1a;
    --accent-red: #e2202a;
  }
  * { box-sizing: border-box; margin: 0; padding: 0; }
  html, body { width: 1200px; height: 586px; overflow: hidden; }
  body {
    background: var(--page);
    font-family: "Exo 2", Arial, sans-serif;
    position: relative;
  }
  .card {
    position: absolute;
    top: 129px;
    width: 502px;
    height: 301px;
    overflow: hidden;
  }
  .card--front { left: 65px; }
  .card--back { left: 608px; }
  .card-texture {
    position: absolute; inset: 0;
    background: linear-gradient(135deg, var(--card-dark-2) 0%, var(--card-dark) 45%, #262626 100%);
  }
  .front-wordmark {
    position: absolute;
    left: 0; right: 0; top: 132px;
    text-align: center;
    color: var(--ink-white);
    font-weight: 600;
    font-size: 38px;
    letter-spacing: 2px;
  }
  .back-light { position: absolute; inset: 0; }
  .back-light svg { position: absolute; inset: 0; }
  .contact { position: absolute; left: 25px; color: var(--ink-white); }
  .contact-name { top: 48px; font-size: 18px; font-weight: 700; }
  .contact-role { top: 72px; font-size: 11.5px; color: var(--ink-soft); }
  .contact-address { top: 134px; font-size: 13px; font-weight: 600; line-height: 17px; }
  .contact-line {
    position: absolute; left: 25px;
    display: flex; align-items: center; gap: 9px;
    font-size: 11.5px; color: var(--ink-white);
  }
  .contact-line svg { width: 13px; height: 12px; flex: none; }
  .line-phone { top: 210px; }
  .line-fax { top: 235px; }
  .line-email { top: 259px; }
  .back-wordmark {
    position: absolute; left: 262px; width: 226px; top: 118px;
    text-align: center;
    font-size: 22px; font-weight: 600; letter-spacing: 1px;
    color: var(--ink-black);
  }
  .brand-row {
    position: absolute; left: 284px; width: 206px; top: 174px;
    display: flex; justify-content: space-between; align-items: center;
    font-size: 9.5px; font-weight: 600; color: var(--ink-black);
    white-space: nowrap;
  }
</style>
</head>
<body>

<section class="card card--front">
  <div class="card-texture" role="img" aria-label="Faint dark low-poly geometric texture"></div>
  <div class="front-wordmark">Kelt Athletic</div>
</section>

<section class="card card--back">
  <div class="card-texture" role="img" aria-label="Faint dark low-poly geometric texture"></div>
  <div class="back-light">
    <svg width="502" height="301" viewBox="0 0 502 301">
      <defs>
        <linearGradient id="lightPanel" x1="0" y1="0" x2="1" y2="1">
          <stop offset="0" stop-color="#ffffff"/>
          <stop offset="0.6" stop-color="#ececec"/>
          <stop offset="1" stop-color="#d8d8d8"/>
        </linearGradient>
      </defs>
      <polygon points="176,0 502,0 502,301 276,301" fill="#ffffff"/>
      <polygon points="183,0 188,0 288,301 283,301" fill="#2b2b2b"/>
      <polygon points="192,0 196,0 296,301 292,301" fill="#ffffff"/>
      <polygon points="200,0 210,0 310,301 300,301" fill="#2b2b2b"/>
      <polygon points="210,0 502,0 502,301 310,301" fill="url(#lightPanel)" role="img" aria-label="Light low-poly geometric texture"/>
    </svg>
  </div>

  <div class="contact contact-name">Dale Fenwick</div>
  <div class="contact contact-role">Managing Director</div>
  <div class="contact contact-address">Elm Yard, Carrow<br>Harlow, HX9 2QT</div>

  <div class="contact-line line-phone">
    <svg viewBox="0 0 13 12"><path fill="var(--accent-red)" d="M1 3.5C1 2 3 1 6.5 1S12 2 12 3.5V5H9.5V3.8h-6V5H1z M3 6h7l1.5 5h-10z"/></svg>
    +44 (0)1632 960418
  </div>
  <div class="contact-line line-fax">
    <svg viewBox="0 0 13 12"><path fill="var(--accent-red)" d="M3.5 1h6v3h-6z M1 4.5h11v5H10v-2H3v2H1z M3.5 8h6v3h-6z"/></svg>
    (555) 014-2237
  </div>
  <div class="contact-line line-email">
    <svg viewBox="0 0 13 12"><path fill="var(--accent-red)" d="M1 2h11v8H1z"/><path fill="none" stroke="#2b2b2b" stroke-width="1.2" d="M1.5 2.5l5 4 5-4"/></svg>
    dale@keltathletic.co.uk
  </div>

  <div class="back-wordmark">Kelt Athletic</div>
  <div class="brand-row">
    <span>Kelt</span>
    <span>PawaLuni</span>
    <span>VerdantFlex</span>
    <span>Grit and Gale</span>
  </div>
</section>

</body>
</html>
```